Ramadan Calander 2023

Design Ramadan product promo calendar. A4 size. Two pages. Front page to have timetable along 4 product promos. Rear Page two have 16 product promos. Must be green and gold. Are free to experiment with shades but cannot be any other colour. Please use new logo as attached. See last years as guide only! we are looking to improve and make stand out more so people will keep it for the month. Experiment with fonts, product orientation and highlights. Please incorporate islamic designs and do not copy past designs be different and original. ...Good Luck
Muslims

```html
<!DOCTYPE html>
<html lang="en">
<head>
<meta charset="utf-8">
<title>Ramadan Timetable 2023 — Zaytun Foods</title>
<link href="https://fonts.googleapis.com/css2?family=Aref+Ruqaa:wght@400;700&family=Great+Vibes&family=Lora:wght@400;500&display=swap" rel="stylesheet">
<style>
  :root {
    --green-deep: #0b3a1f;
    --green-mid: #15532c;
    --green-bright: #0f6b38;
    --green-light: #3f8a48;
    --ink: #070d09;
    --gold: #e7c35a;
    --gold-soft: #f2d98a;
    --gold-dark: #a8772a;
    --cream: #f4f1e6;
  }
  * { margin: 0; padding: 0; box-sizing: border-box; }
  html, body { width: 848px; height: 1200px; overflow: hidden; background: var(--green-deep); }
  .page {
    position: relative; width: 848px; height: 1200px; overflow: hidden;
    background: linear-gradient(180deg, var(--green-deep) 0%, var(--green-mid) 60%, var(--green-light) 100%);
    font-family: "Lora", Georgia, serif; color: var(--cream);
  }
  .frame { position: absolute; inset: 0; }
  .skyline {
    position: absolute; left: 48px; top: 660px; width: 752px; height: 370px;
  }
  .title { position: absolute; left: 0; width: 848px; text-align: center; }
  .title-year { top: 136px; font-family: "Aref Ruqaa", serif; font-weight: 700; font-size: 40px; color: var(--gold); line-height: 1; }
  .title-main { top: 172px; font-family: "Aref Ruqaa", serif; font-weight: 700; font-size: 50px; color: var(--gold); line-height: 1; }
  .title-sub { top: 216px; font-family: "Great Vibes", cursive; font-size: 32px; color: var(--gold); line-height: 1; padding-left: 20px; }
  .title-table { top: 258px; font-family: "Aref Ruqaa", serif; font-weight: 700; font-size: 38px; color: var(--cream); line-height: 1; }

  .timetable-head {
    position: absolute; left: 140px; top: 312px; width: 578px; height: 31px;
    background: var(--green-bright); border-radius: 4px;
    display: grid; grid-template-columns: 32px 126px 54px 102px 56px 84px 56px 68px;
    align-items: center; text-align: center;
    font-family: "Aref Ruqaa", serif; font-weight: 700; font-size: 16px; color: var(--cream);
  }
  .timetable-head .col-gold { color: var(--gold); }

  .timetable {
    position: absolute; left: 140px; top: 353px; width: 578px;
    border-collapse: collapse; table-layout: fixed;
    font-size: 15.5px; line-height: 17.15px;
  }
  .timetable td { height: 17.15px; padding: 0; text-align: center; white-space: nowrap; }
  .timetable td.sehri, .timetable td.iftar { color: var(--gold); }
  .timetable tr.friday td { background: var(--green-bright); }
  .timetable tr.friday td:first-child { border-radius: 4px 0 0 4px; }
  .timetable tr.friday td:last-child { border-radius: 0 4px 4px 0; }

  .note {
    position: absolute; left: 0; top: 889px; width: 848px; text-align: center;
    font-size: 15.5px; line-height: 17.2px; color: var(--gold-soft);
  }
  .brand {
    position: absolute; left: 0; top: 958px; width: 848px; text-align: center;
    font-family: "Lora", serif; font-weight: 500; color: var(--gold); line-height: 1;
  }
  .brand-name { font-size: 34px; letter-spacing: 10px; }
  .brand-line { display: block; font-size: 13px; letter-spacing: 8px; margin-top: 6px; }

  .promo {
    position: absolute; top: 1027px; width: 152px; height: 152px;
    background: linear-gradient(180deg, #3a3520 0%, #2f4a2a 50%, #3f8a48 100%);
  }
  .promo-price {
    position: absolute; left: 0; bottom: 6px; width: 100%; text-align: center;
    font-family: "Aref Ruqaa", serif; font-weight: 700; font-size: 26px; color: var(--gold);
  }
</style>
</head>
<body>
<main class="page">
  <svg class="frame" width="848" height="1200" viewBox="0 0 848 1200" aria-hidden="true">
    <defs>
      <linearGradient id="archFill" x1="0" y1="0" x2="0" y2="1">
        <stop offset="0" stop-color="#050a07"/>
        <stop offset="0.5" stop-color="#08160d"/>
        <stop offset="1" stop-color="#0f4424"/>
      </linearGradient>
    </defs>
    <line x1="133" y1="23" x2="715" y2="23" stroke="var(--gold)" stroke-width="1.5"/>
    <path d="M0,340 L0,300 Q30,260 80,255 L185,250 Q240,190 300,160 Q370,128 390,95 Q405,50 424,48 Q443,50 458,95 Q478,128 548,160 Q608,190 663,250 L768,255 Q818,260 848,300 L848,340 Z"
          fill="var(--green-bright)" stroke="var(--gold)" stroke-width="3"/>
    <path d="M18,1200 V345 Q18,300 70,292 L200,285 Q250,220 310,190 Q385,150 405,110 Q415,85 424,80 Q433,85 443,110 Q463,150 538,190 Q598,220 648,285 L778,292 Q830,300 830,345 V1200 Z"
          fill="url(#archFill)"/>
    <line x1="18" y1="340" x2="18" y2="1200" stroke="var(--gold)" stroke-width="1.2"/>
    <line x1="830" y1="340" x2="830" y2="1200" stroke="var(--gold)" stroke-width="1.2"/>
    <line x1="93" y1="290" x2="93" y2="512" stroke="var(--gold)" stroke-width="1"/>
    <line x1="755" y1="290" x2="755" y2="512" stroke="var(--gold)" stroke-width="1"/>
  </svg>

  <svg class="skyline" role="img" aria-label="Mosque silhouette with domes and minarets" viewBox="0 0 752 370" preserveAspectRatio="none">
    <defs>
      <linearGradient id="skylineFill" x1="0" y1="0" x2="0" y2="1">
        <stop offset="0" stop-color="#050a07" stop-opacity="0"/>
        <stop offset="0.35" stop-color="#050a07" stop-opacity="0.55"/>
        <stop offset="1" stop-color="#050a07" stop-opacity="0.85"/>
      </linearGradient>
    </defs>
    <rect width="752" height="370" fill="url(#skylineFill)"/>
  </svg>

  <div class="title title-year">2023</div>
  <div class="title title-main">Ramadan</div>
  <div class="title title-sub">Kareem</div>
  <h1 class="title title-table">Ramadan Timetable</h1>

  <div class="timetable-head">
    <span>Fast</span><span>Date</span><span>Day</span><span class="col-gold">Sehri Ends</span>
    <span>Zhur</span><span>Asr</span><span class="col-gold">Iftar</span><span>Isha</span>
  </div>

  <table class="timetable">
    <colgroup>
      <col style="width:32px"><col style="width:126px"><col style="width:54px"><col style="width:102px">
      <col style="width:56px"><col style="width:84px"><col style="width:56px"><col style="width:68px">
    </colgroup>
    <tbody>
      <tr><td></td><td>March 21</td><td>Wed</td><td class="sehri">3.53</td><td>1.08</td><td>5.47</td><td class="iftar">8.01</td><td>9.24</td></tr>
      <tr><td>1</td><td>March 22</td><td>Thur</td><td class="sehri">3.51</td><td>1.08</td><td>5.48</td><td class="iftar">8.02</td><td>9.26</td></tr>
      <tr class="friday"><td>2</td><td>March 23</td><td>Fri</td><td class="sehri">3.49</td><td>1.07</td><td>5.49</td><td class="iftar">8.04</td><td>9.27</td></tr>
      <tr><td>3</td><td>March 24</td><td>Sat</td><td class="sehri">3.47</td><td>1.07</td><td>5.51</td><td class="iftar">8.06</td><td>9.29</td></tr>
      <tr><td>4</td><td>March 25</td><td>Sun</td><td class="sehri">3.45</td><td>1.07</td><td>5.52</td><td class="iftar">8.07</td><td>9.30</td></tr>
      <tr><td>5</td><td>March 26</td><td>Mon</td><td class="sehri">3.43</td><td>1.07</td><td>5.53</td><td class="iftar">8.09</td><td>9.31</td></tr>
      <tr><td>6</td><td>March 27</td><td>Tue</td><td class="sehri">3.40</td><td>1.06</td><td>5.54</td><td class="iftar">8.11</td><td>9.33</td></tr>
      <tr><td>7</td><td>March 28</td><td>Wed</td><td class="sehri">3.38</td><td>1.06</td><td>5.55</td><td class="iftar">8.12</td><td>9.35</td></tr>
      <tr><td>8</td><td>March 29</td><td>Thur</td><td class="sehri">3.36</td><td>1.06</td><td>5.56</td><td class="iftar">8.14</td><td>9.37</td></tr>
      <tr class="friday"><td>9</td><td>March 30</td><td>Fri</td><td class="sehri">3.34</td><td>1.06</td><td>5.57</td><td class="iftar">8.16</td><td>9.38</td></tr>
      <tr><td>10</td><td>March 31</td><td>Sat</td><td class="sehri">3.32</td><td>1.06</td><td>5.58</td><td class="iftar">8.17</td><td>9.39</td></tr>
      <tr><td>11</td><td>April 1</td><td>Sun</td><td class="sehri">3.30</td><td>1.05</td><td>5.59</td><td class="iftar">8.19</td><td>9.41</td></tr>
      <tr><td>12</td><td>April 2</td><td>Mon</td><td class="sehri">3.30</td><td>1.05</td><td>6.00</td><td class="iftar">8.21</td><td>9.42</td></tr>
      <tr><td>13</td><td>April 3</td><td>Tue</td><td class="sehri">3.29</td><td>1.05</td><td>6.01</td><td class="iftar">8.22</td><td>9.43</td></tr>
      <tr><td>14</td><td>April 4</td><td>Wed</td><td class="sehri">3.28</td><td>1.05</td><td>6.02</td><td class="iftar">8.24</td><td>9.45</td></tr>
      <tr><td>15</td><td>April 5</td><td>Thur</td><td class="sehri">3.27</td><td>1.05</td><td>6.03</td><td class="iftar">8.26</td><td>9.46</td></tr>
      <tr class="friday"><td>16</td><td>April 6</td><td>Fri</td><td class="sehri">3.26</td><td>1.05</td><td>6.05</td><td class="iftar">8.27</td><td>9.46</td></tr>
      <tr><td>17</td><td>April 7</td><td>Sat</td><td class="sehri">3.26</td><td>1.05</td><td>6.06</td><td class="iftar">8.29</td><td>9.49</td></tr>
      <tr><td>18</td><td>April 8</td><td>Sun</td><td class="sehri">3.25</td><td>1.05</td><td>6.06</td><td class="iftar">8.30</td><td>9.50</td></tr>
      <tr><td>19</td><td>April 9</td><td>Mon</td><td class="sehri">3.25</td><td>1.06</td><td>6.08</td><td class="iftar">8.32</td><td>9.51</td></tr>
      <tr><td>20</td><td>April 10</td><td>Tue</td><td class="sehri">3.25</td><td>1.06</td><td>6.09</td><td class="iftar">8.34</td><td>9.53</td></tr>
      <tr><td>21</td><td>April 11</td><td>Wed</td><td class="sehri">3.24</td><td>1.06</td><td>6.10</td><td class="iftar">8.35</td><td>9.55</td></tr>
      <tr><td>22</td><td>April 12</td><td>Thur</td><td class="sehri">3.23</td><td>1.06</td><td>6.10</td><td class="iftar">8.37</td><td>9.56</td></tr>
      <tr class="friday"><td>23</td><td>April 13</td><td>Fri</td><td class="sehri">3.22</td><td>1.06</td><td>6.11</td><td class="iftar">8.39</td><td>9.58</td></tr>
      <tr><td>24</td><td>April 14</td><td>Sat</td><td class="sehri">3.22</td><td>1.07</td><td>6.12</td><td class="iftar">8.40</td><td>9.59</td></tr>
      <tr><td>25</td><td>April 15</td><td>Sun</td><td class="sehri">3.21</td><td>1.07</td><td>6.13</td><td class="iftar">8.42</td><td>10.01</td></tr>
      <tr><td>26</td><td>April 16</td><td>Mon</td><td class="sehri">3.21</td><td>1.07</td><td>6.14</td><td class="iftar">8.43</td><td>10.02</td></tr>
      <tr><td>27</td><td>April 17</td><td>Tue</td><td class="sehri">3.20</td><td>1.07</td><td>6.15</td><td class="iftar">8.45</td><td>10.04</td></tr>
      <tr><td>28</td><td>April 18</td><td>Wed</td><td class="sehri">3.19</td><td>1.07</td><td>6.16</td><td class="iftar">8.46</td><td>10.05</td></tr>
      <tr><td>29</td><td>April 19</td><td>Thur</td><td class="sehri">3.18</td><td>1.07</td><td>6.17</td><td class="iftar">8.48</td><td>10.07</td></tr>
      <tr class="friday"><td>30</td><td>April 20</td><td>Fri</td><td class="sehri">3.17</td><td>1.07</td><td>6.18</td><td class="iftar">8.50</td><td>10.08</td></tr>
    </tbody>
  </table>

  <p class="note">Lorem ipsum dolor sit amet, consectetuer adipiscing elit, sed diam<br>nonummy nibh euismod tincidunt ut laoreet dolore magna<br>aliquam erat volutpat. Ut wisi enim ad minim veniam, quis nostrud</p>

  <div class="brand">
    <span class="brand-name">ZAYTUN</span>
    <span class="brand-line">FOODS</span>
  </div>

  <div class="promo" style="left:65px" role="img" aria-label="Product photo for promotion one"><span class="promo-price">2 for $9</span></div>
  <div class="promo" style="left:253px" role="img" aria-label="Product photo for promotion two"><span class="promo-price">$9.97</span></div>
  <div class="promo" style="left:443px" role="img" aria-label="Product photo for promotion three"><span class="promo-price">$24.9</span></div>
  <div class="promo" style="left:632px" role="img" aria-label="Product photo for promotion four"><span class="promo-price">2 for $9</span></div>
</main>
</body>
</html>
```